Business Consulting Website Design

UPDATED KEY MESSAGES:

The client has decided o a different direction.

The Key Messages include:
-- Creating something unique.
Every company is unique, ever culture unique. Every project customized to meet the unique needs of the client. No two things are alike.
-- One of a kind
Because every company is different, every culture is different, every objective is unique
-- Customized solutions
We create something just for you …

I think the approach needs to be about creating a masterpiece as opposed to nurturing/growing.

Perhaps we could have different abstract/colorful paint items that takes up part of the page for each landing page. Against white and on the white is where we put our text.

Client also has created a Pixelgrove Lightbox with images that she likes

http://www.pixelgrove-demo.com/public_lightbox.mhtml?code=a9d3c5e7b1f2046d8e3a7c9b5f1d2e46&lightbox_id=58210477

She also likes the watercolor look against white background.

===============================
Need a Homepage and an Interior page redesign for my client: http://www.talvoremethods-demo.com

Client does leadership development, performance management, talent development, etc. Has some great clients.

- This site is very old and needs a modern look. Update look & colors. She wants simple but not bland.
- Banner images should be interesting.
- She likes the purple in her logo
- She thinks Arial font is outdated and boring
- We will be rewriting all the copy.
- Design should include Connectly icon, phone, email, and address
- She likes the client grid on the Our Clients page. We will be redoing this.

- Menus will include:
-- Home
-- What We Do
-- Who We Are
-- Our Clients
-- Snapshots (these are case studies)

One of the sites she liked is http://quillbound-anthem.com, though this website has much more content than she will have.

I'm attaching the following files for your reference:
- Her new business card proof that contains her logo
- a zip file containing some stock image comps

Need strong design. Site will likely be built in Wordpress.

Thanks,
Nora

Target Market(s)

SVP of Human Resources or Head of Talent

Industry/Entity Type

Business

Number of Pages Required

2 page

Font styles to use
Sans Serif

Colors
b768aa
876aae
6b449b
f04a50
f37122

Requirements
Must have
• - Designer must read the brief
• - Use logo
Nice to have
• - Strong banner images to complement the key message
• - Design will function work on mobile easily
Should not have
• - Should not look like a design template was purchased from layoutbarn-demo.com or other template sites.
• - Should not be too masculine
• - Should not feel cluttered.

```html
<!DOCTYPE html>
<html lang="en">
<head>
<meta charset="utf-8">
<title>Talvore Methods Incorporated</title>
<link href="https://fonts.googleapis.com/css2?family=Montserrat:ital,wght@0,400;0,600;0,700;1,700&family=Raleway:wght@300;400;500;600&display=swap" rel="stylesheet">
<style>
  :root {
    --purple-deep: #5b2c86;
    --purple: #6b449b;
    --purple-nav: #9a7ab9;
    --purple-footer: #765fa0;
    --pink-band: #c0648f;
    --magenta: #e0309a;
    --orange: #f37122;
    --grey-text: #555;
    --grey-line: #c9c9c9;
    --circle: #bdbdbd;
    --white: #fff;
    --ink: #222;
  }
  * { margin: 0; padding: 0; box-sizing: border-box; }
  html, body { width: 1200px; height: 2315px; overflow: hidden; background: var(--white); }
  body { position: relative; font-family: "Raleway", Arial, sans-serif; color: var(--ink); }

  .site-header { position: absolute; top: 0; left: 0; width: 1200px; height: 330px; background: var(--white); }
  .brand { position: absolute; left: 58px; top: 80px; display: flex; align-items: center; gap: 18px; }
  .brand-square { width: 44px; height: 44px; background: var(--purple); }
  .brand-name { font-family: "Raleway", sans-serif; font-weight: 500; color: var(--purple); font-size: 38px; line-height: 1.2; letter-spacing: 6px; text-transform: uppercase; }
  .brand-name small { display: block; font-size: 22px; letter-spacing: 5px; }
  .header-art { position: absolute; right: 0; top: 0; width: 640px; height: 170px; background: linear-gradient(200deg, #d9d9d9 0%, #f2f2f2 45%, var(--white) 80%); }
  .social { position: absolute; right: 62px; top: 168px; display: flex; gap: 18px; font-family: "Montserrat", sans-serif; font-weight: 700; font-size: 17px; color: var(--ink); }
  .header-rule { position: absolute; right: 62px; top: 212px; width: 300px; height: 2px; background: var(--purple); }
  .header-phone { position: absolute; right: 62px; top: 228px; display: flex; align-items: center; gap: 14px; font-size: 38px; color: var(--purple); font-weight: 400; }

  .main-nav { position: absolute; top: 330px; left: 0; width: 1200px; height: 65px; background: var(--purple-nav); }
  .main-nav a { position: absolute; top: 20px; transform: translateX(-50%); font-family: "Montserrat", sans-serif; font-weight: 600; font-size: 20px; color: var(--white); text-decoration: none; white-space: nowrap; }

  .hero { position: absolute; top: 395px; left: 0; width: 1200px; height: 590px;
    background: linear-gradient(90deg, #e04fc6 0%, #f08ad9 14%, #f5a3b0 26%, #f2553d 40%, #f58a1c 55%, #f7c21b 68%, #c9d92a 82%, #4fbf2a 100%); }
  .hero-title { position: absolute; top: 240px; width: 100%; text-align: center; font-family: "Montserrat", sans-serif; font-weight: 700; font-size: 48px; color: var(--purple-deep); }
  .hero-title em { font-style: italic; }
  .btn-learn { position: absolute; top: 330px; left: 475px; width: 253px; height: 64px; border-radius: 32px; background: linear-gradient(#8a5aa6, #5c2e7e); box-shadow: 0 4px 8px rgba(0,0,0,.3); display: flex; align-items: center; justify-content: space-between; padding: 0 8px 0 30px; font-family: "Montserrat", sans-serif; font-weight: 700; font-size: 25px; color: var(--white); text-decoration: none; }
  .btn-learn span.arrow { width: 48px; height: 48px; border-radius: 50%; background: var(--white); display: flex; align-items: center; justify-content: center; }

  .intro { position: absolute; top: 1015px; left: 0; width: 1200px; height: 225px; }
  .side-menu { position: absolute; left: 150px; top: 45px; list-style: none; font-family: "Montserrat", sans-serif; font-weight: 600; font-size: 20px; line-height: 29px; color: var(--ink); }
  .intro-divider { position: absolute; left: 312px; top: 0; width: 2px; height: 225px; background: var(--ink); }
  .intro-text { position: absolute; left: 330px; width: 720px; top: 64px; text-align: center; font-family: "Montserrat", sans-serif; font-weight: 600; font-size: 24px; line-height: 37px; color: var(--purple); }

  .offer { position: absolute; top: 1288px; left: 52px; width: 1103px; height: 102px; border: 2px solid #ddd; }
  .offer h2 { position: absolute; top: -20px; left: 50%; transform: translateX(-50%); background: var(--white); padding: 0 58px; font-family: "Montserrat", sans-serif; font-weight: 700; font-size: 25px; color: var(--magenta); white-space: nowrap; }
  .offer p { position: absolute; top: 50px; width: 100%; text-align: center; font-size: 22px; color: var(--grey-text); }

  .strengths { position: absolute; top: 1452px; left: 0; width: 1200px; height: 238px; background: linear-gradient(90deg, #0b0b0b 0%, #2a2a2a 35%, #5a5a5a 60%, #2b2b2b 100%); }
  .strength { position: absolute; top: 32px; width: 180px; height: 180px; border-radius: 50%; background: var(--circle); display: flex; align-items: center; justify-content: center; text-align: center; font-family: "Montserrat", sans-serif; font-weight: 600; font-size: 20px; line-height: 27px; color: #333; }

  .tagline { position: absolute; top: 1690px; left: 0; width: 1200px; height: 150px; background: var(--pink-band); text-align: center; color: var(--white); font-family: "Montserrat", sans-serif; }
  .tagline .kicker { margin-top: 38px; font-size: 22px; font-weight: 600; letter-spacing: 3px; }
  .tagline .headline { margin-top: 6px; font-size: 37px; font-weight: 700; }

  .site-footer { position: absolute; top: 1840px; left: 0; width: 1200px; height: 345px; background: var(--purple-footer); color: var(--white); }
  .site-footer .brand { left: 112px; top: 120px; }
  .site-footer .brand-square { background: var(--white); }
  .site-footer .brand-name { color: var(--white); }
  .footer-rule { position: absolute; left: 528px; width: 610px; height: 2px; background: rgba(255,255,255,.35); }
  .footer-phone { position: absolute; left: 530px; top: 102px; display: flex; align-items: center; gap: 16px; font-size: 46px; }
  .footer-email { position: absolute; left: 530px; top: 203px; font-size: 36px; font-weight: 500; }

  .legal { position: absolute; top: 2200px; left: 0; width: 1200px; text-align: center; font-size: 16px; line-height: 26px; color: var(--ink); }
</style>
</head>
<body>

<header class="site-header">
  <div class="brand">
    <span class="brand-square"></span>
    <div class="brand-name">Talvore<br>Methods<small>Incorporated</small></div>
  </div>
  <div class="header-art" role="img" aria-label="Close-up of a fine paintbrush tip on white"></div>
  <nav class="social" aria-label="Social links"><span>Connectly</span><span>Friendloop</span><span>Chirpline</span></nav>
  <div class="header-rule"></div>
  <div class="header-phone">
    <svg width="40" height="40" viewBox="0 0 24 24" aria-hidden="true"><path fill="#333" d="M6.6 10.8c1.4 2.8 3.8 5.1 6.6 6.6l2.2-2.2c.3-.3.7-.4 1-.2 1.1.4 2.3.6 3.6.6.6 0 1 .4 1 1V20c0 .6-.4 1-1 1C10.6 21 3 13.4 3 4c0-.6.4-1 1-1h3.5c.6 0 1 .4 1 1 0 1.3.2 2.5.6 3.6.1.3 0 .7-.2 1z"/></svg>
    <span>555.014.2288</span>
  </div>
</header>

<nav class="main-nav" aria-label="Main">
  <a href="#" style="left:236px">Home</a>
  <a href="#" style="left:401px">What We Do</a>
  <a href="#" style="left:596px">Who We Are</a>
  <a href="#" style="left:784px">Our Clients</a>
  <a href="#" style="left:943px">Snapshots</a>
</nav>

<section class="hero" role="img" aria-label="Vertical watercolor stripes in magenta, pink, red, orange, yellow and green">
  <h1 class="hero-title"><em>Creating</em>......just for you</h1>
  <a class="btn-learn" href="#">Learn More
    <span class="arrow"><svg width="26" height="26" viewBox="0 0 24 24" aria-hidden="true"><path fill="#6b449b" d="M8 4l8 8-8 8-2-2 6-6-6-6z"/></svg></span>
  </a>
</section>

<section class="intro">
  <ul class="side-menu">
    <li>Home</li><li>What We Do</li><li>Who We Are</li><li>Our Clients</li><li>Snapshots</li>
  </ul>
  <div class="intro-divider"></div>
  <p class="intro-text">We works on the frontlines of international development.<br>Transforming ideas into action—action into impact.<br>We are committed to shaping a more livable world.</p>
</section>

<section class="offer">
  <h2>WHAT CAN TMI DO FOR YOU?</h2>
  <p>We will craft a customized plan of services to meet each client’s unique needs.</p>
</section>

<section class="strengths" role="img" aria-label="Monochrome fan of white pencils with one purple pencil rising">
  <div class="strength" style="left:218px">Experience<br>Counts</div>
  <div class="strength" style="left:418px">Exceptional<br>Service</div>
  <div class="strength" style="left:617px">On time<br>On budget</div>
  <div class="strength" style="left:810px">Your<br>Resource</div>
</section>

<section class="tagline">
  <p class="kicker">designing, developing &amp; implementing</p>
  <p class="headline">HUMAN RESOURCE COMMUNICATIONS</p>
</section>

<footer class="site-footer">
  <div class="brand">
    <span class="brand-square"></span>
    <div class="brand-name">Talvore<br>Methods<small>Incorporated</small></div>
  </div>
  <div class="footer-rule" style="top:88px"></div>
  <div class="footer-phone">
    <svg width="46" height="46" viewBox="0 0 24 24" aria-hidden="true"><path fill="#f5a46a" d="M6.6 10.8c1.4 2.8 3.8 5.1 6.6 6.6l2.2-2.2c.3-.3.7-.4 1-.2 1.1.4 2.3.6 3.6.6.6 0 1 .4 1 1V20c0 .6-.4 1-1 1C10.6 21 3 13.4 3 4c0-.6.4-1 1-1h3.5c.6 0 1 .4 1 1 0 1.3.2 2.5.6 3.6.1.3 0 .7-.2 1z"/></svg>
    <span>555.014.2288</span>
  </div>
  <div class="footer-rule" style="top:190px"></div>
  <p class="footer-email">Mara@TalvoreMethods.com</p>
</footer>

<p class="legal">Copyright &nbsp;2015, Talvore Methods.<br>Legal conditions and terms of use applicable to all users of this site.<br>Any use of this site constitutes your agreement to the terms and conditions and the operating policies.</p>

</body>
</html>
```